Roofing Company Modern look

I want a modern and sophisticated look for our roofing business.

Our address is :

4276 Pellman Crossing Rd
Orlando, Fl 32825

(407)-583-2716

www.SummitcrestShinglesFl.com

I also want to make sure on the back there is a spot to put
Project Manager Name :

Number:

Because the cards will be used by all sales people

Project Manager Name :

Also there are accreditation we have logos are uploaded here as well that I would like maybe on the back of card as well

I also want to highlight our special attributions or trades:

Residential & Commercial
Fully Insured
License # CCC4872196
Insurance Claims
Serving Central Florida Since 1992
Free Estimates

Contact Information for Business Card

Our address is :

4276 Pellman Crossing Rd
Orlando, Fl 32825

(407)-583-2716

Project Manager Name :

Residential & Commercial
Fully Insured
License # CCC4872196
Insurance Claims
Free Estimates

Font styles to use
Serif
Sans Serif

Colors
3176b5

Requirements
Must have
• Must have royal blue like my logo grey and black are the colors I like

```html
<!DOCTYPE html>
<html lang="en">
<head>
<meta charset="utf-8">
<title>Summitcrest Roofing &amp; Gutters – Business Card</title>
<link rel="stylesheet" href="https://fonts.googleapis.com/css2?family=Roboto:wght@300;400;500&display=swap">
<style>
  :root {
    --royal-blue: #3176b5;
    --bright-blue: #2f86d6;
    --ink: #0f0f11;
    --paper: #f7f7f6;
    --grey-text: #555a60;
    --grey-light: #a3a7ac;
    --grey-rule: #8a8d91;
    --backdrop: #e9e9e8;
  }
  * { box-sizing: border-box; margin: 0; padding: 0; }
  html, body { width: 1200px; height: 900px; overflow: hidden; }
  body {
    background: var(--backdrop);
    font-family: "Roboto", Arial, sans-serif;
    font-weight: 300;
    display: flex;
    align-items: center;
    justify-content: center;
    gap: 80px;
  }
  .card {
    width: 340px;
    height: 595px;
    position: relative;
    display: flex;
    flex-direction: column;
    align-items: center;
    box-shadow: 0 18px 40px rgba(0,0,0,0.18);
  }
  .card--front { background: var(--paper); color: var(--grey-text); }
  .card--back { background: var(--ink); color: var(--grey-light); }

  .brand { display: flex; flex-direction: column; align-items: center; margin-top: 64px; }
  .brand__dot { width: 46px; height: 46px; border-radius: 50%; background: var(--royal-blue); margin-bottom: 14px; }
  .brand__name {
    font-size: 34px; font-weight: 400; letter-spacing: 2px;
    color: var(--royal-blue); text-transform: uppercase; line-height: 1;
  }
  .brand__tagline {
    font-size: 11px; font-weight: 400; letter-spacing: 1.6px;
    color: var(--royal-blue); text-transform: uppercase; margin-top: 6px;
  }

  .fill-line { width: 200px; height: 1px; background: var(--grey-rule); }
  .fill-lines { display: flex; flex-direction: column; gap: 56px; margin-top: 60px; }

  .rule { width: 28px; height: 2px; background: var(--royal-blue); }

  .contact { display: flex; flex-direction: column; align-items: center; margin-top: 44px; }
  .contact__icons { display: flex; gap: 8px; margin: 14px 0 8px; }
  .contact__icons svg { width: 16px; height: 16px; }
  .contact__line { font-size: 15px; line-height: 1.35; text-align: center; }

  .badges { display: grid; grid-template-columns: repeat(2, 58px); gap: 12px 22px; margin-top: 26px; }
  .badge { height: 36px; border-radius: 4px; }
  .badge--navy { background: #2b4a7e; }
  .badge--red { background: #c8232c; }
  .badge--round { width: 36px; border-radius: 50%; background: #c6c9cc; justify-self: center; }
  .badge--blue { background: #3b78b3; height: 44px; }

  .card--back .brand { margin-top: 110px; }
  .card--back .rule { margin-top: 60px; }
  .attributes { list-style: none; text-align: center; margin: 22px 0; font-size: 15px; line-height: 1.6; }
  .website { margin-top: 70px; font-size: 14px; color: var(--bright-blue); font-weight: 400; }
</style>
</head>
<body>
  <section class="card card--front">
    <div class="brand">
      <span class="brand__dot"></span>
      <span class="brand__name">Summitcrest</span>
      <span class="brand__tagline">Roofing &amp; Gutters Inc.</span>
    </div>
    <div class="fill-lines">
      <span class="fill-line"></span>
      <span class="fill-line"></span>
    </div>
    <div class="contact">
      <span class="rule"></span>
      <div class="contact__icons">
        <svg viewBox="0 0 16 16" aria-label="Phone"><circle cx="8" cy="8" r="7" fill="none" stroke="var(--royal-blue)" stroke-width="1.2"/><path d="M5.5 4.8l1.3-.3.8 1.8-.8.7c.4.9 1 1.5 1.9 1.9l.7-.8 1.8.8-.3 1.3c-2.9.1-5.5-2.5-5.4-5.4z" fill="var(--royal-blue)"/></svg>
        <svg viewBox="0 0 16 16" aria-label="Location"><circle cx="8" cy="8" r="7" fill="none" stroke="var(--royal-blue)" stroke-width="1.2"/><path d="M8 3.8a2.6 2.6 0 0 0-2.6 2.6c0 2 2.6 5 2.6 5s2.6-3 2.6-5A2.6 2.6 0 0 0 8 3.8zm0 3.6a1 1 0 1 1 0-2 1 1 0 0 1 0 2z" fill="var(--royal-blue)"/></svg>
      </div>
      <p class="contact__line">(407) 583 2716</p>
      <p class="contact__line">4276 Pellman Crossing Rd</p>
      <p class="contact__line">Orlando, Fl 32825</p>
    </div>
    <div class="badges" aria-label="Accreditations">
      <span class="badge badge--navy"></span>
      <span class="badge badge--round"></span>
      <span class="badge badge--red"></span>
      <span class="badge badge--blue"></span>
    </div>
  </section>

  <section class="card card--back">
    <div class="brand">
      <span class="brand__dot"></span>
      <span class="brand__name">Summitcrest</span>
      <span class="brand__tagline">Roofing &amp; Gutters LLC</span>
    </div>
    <span class="rule"></span>
    <ul class="attributes">
      <li>Residential &amp; Commercial</li>
      <li>Fully Insured</li>
      <li>License # CCC4872196</li>
      <li>Insurance Claims</li>
      <li>Serving Central Florida Since 1992</li>
      <li>Free Estimates</li>
    </ul>
    <span class="rule" style="margin-top:0"></span>
    <p class="website">www.SummitcrestShinglesFl.com</p>
  </section>
</body>
</html>
```